MRHT Needs Fundraiser Dinner Invite!!

The Marisol Hendrick Trust, a 501 3(c) non for profit has a yearly fundraiser, with varying themes. Last year it was "cowboys" and "cowgirls"
This year, it is Club Orchid, or 70's disco music. I have uploaded last years invite for reference, some stock photography for inspiration. You are not limited to using the stock photos.

Annual MRHT Fundraiser Dinner
October 13th, 2022
Starts: 6:30pm
RSVP By: September 20th
Place: The Bramwell
Price: $135 per ticket

Target Market(s)

Donors, Business People, Every person

Industry/Entity Type

Non for Profit

Font styles to use
Sans Serif

Colors
0054AA
0677BA
7BADD7
CADEEF
E8F1F8
E54698
E96AAD
F1A4CE
F9D9EA
FCEFF6
6B429C
8869AF
B7A5CE
E3DAEB
F3F0F8

Requirements
Must have
• The invite should be 5x7, be sophisticated as the clientele are mainly business people that come to support the cause. It should be fun and inviting at the same time.

```html
<!DOCTYPE html>
<html lang="en">
<head>
<meta charset="utf-8">
<title>Annual MRHT Fundraiser Dinner – Invite</title>
<link rel="stylesheet" href="https://fonts.googleapis.com/css2?family=Archivo:wdth,wght@62..125,400..900&display=swap">
<style>
  :root {
    --backdrop: #1c1c1c;
    --violet-deep: #5a1fd6;
    --violet: #7a2cf0;
    --magenta: #c628c9;
    --pink: #e54698;
    --pink-hot: #f03fb0;
    --ring-dark: #4a167f;
    --band-violet: #6b2cff;
    --band-text: #efe4ff;
    --band-black: #1d1a22;
    --ink-light: #ffffff;
    --pearl-light: #fff3fb;
    --pearl-mid: #f1a4ce;
    --pearl-edge: #b07ad8;
  }
  * { box-sizing: border-box; margin: 0; padding: 0; }
  html, body {
    width: 1200px; height: 960px; overflow: hidden;
    background: var(--backdrop);
    font-family: "Archivo", "Helvetica Neue", Arial, sans-serif;
  }
  .invite {
    position: absolute; left: 280px; top: 32px;
    width: 640px; height: 896px; overflow: hidden;
    background: linear-gradient(160deg, var(--violet-deep) 0%, var(--magenta) 38%, var(--pink-hot) 62%, var(--magenta) 85%, var(--violet) 100%);
    color: var(--ink-light);
  }
  .rings { position: absolute; inset: 0; }
  .label {
    position: absolute;
    font-stretch: 125%; font-weight: 500;
    font-size: 18px; letter-spacing: 0.14em; text-transform: uppercase;
    white-space: nowrap;
  }
  .doors { left: 16px; top: 28px; }
  .price { right: 20px; bottom: 22px; }
  .date {
    left: 628px; top: 36px;
    transform-origin: 0 0; transform: rotate(90deg);
  }
  .rsvp {
    left: 16px; top: 888px;
    transform-origin: 0 0; transform: rotate(-90deg);
  }
  .annual {
    position: absolute; left: 0; right: 0; top: 160px;
    text-align: center;
    font-stretch: 125%; font-weight: 500; font-size: 76px;
    letter-spacing: 0.1em; line-height: 1;
  }
  .disco-ball {
    position: absolute; left: 196px; top: 260px; width: 288px; height: 288px;
    border-radius: 50%;
    background: radial-gradient(circle at 38% 30%, #ffd2f4 0%, #e37ee6 30%, #b743d6 62%, #7a1ea8 100%);
  }
  .title {
    position: absolute; left: 0; top: 250px; width: 640px; height: 300px;
  }
  .title text {
    font-family: "Archivo", "Arial Black", sans-serif;
    font-weight: 900; font-size: 250px;
  }
  .band-event {
    position: absolute; left: 90px; top: 562px; width: 484px; height: 60px;
    background: var(--band-violet);
    color: var(--band-text);
    display: flex; align-items: center; justify-content: center;
    font-stretch: 125%; font-weight: 600; font-size: 27px; letter-spacing: 0.08em;
  }
  .band-host {
    position: absolute; left: 96px; top: 650px; width: 496px; height: 46px;
    background: var(--band-black);
    transform: rotate(-3deg);
    display: flex; align-items: center; justify-content: center;
    font-stretch: 125%; font-weight: 600; font-size: 17px; letter-spacing: 0.08em;
    text-transform: uppercase;
  }
  .pearl {
    position: absolute; border-radius: 50%;
    background: radial-gradient(circle at 35% 30%, var(--pearl-light) 0%, var(--pearl-mid) 45%, var(--pearl-edge) 100%);
  }
  .butterfly {
    position: absolute; border-radius: 50%;
    background: radial-gradient(ellipse, rgba(255,255,255,0.55) 0%, rgba(255,255,255,0.15) 60%, rgba(255,255,255,0) 75%);
  }
  .host-mark {
    position: absolute; left: 72px; top: 836px;
    display: flex; align-items: center; gap: 8px;
    font-weight: 500; font-size: 15px; letter-spacing: 0.02em;
    color: var(--pearl-light);
  }
  .host-mark .dot { width: 12px; height: 12px; border-radius: 50%; background: var(--pearl-light); }
</style>
</head>
<body>
  <main class="invite">
    <svg class="rings" width="640" height="896" viewBox="0 0 640 896" aria-hidden="true">
      <defs>
        <radialGradient id="ring-fill" cx="340" cy="404" r="520" gradientUnits="userSpaceOnUse">
          <stop offset="0" stop-color="#9a2bd8"/>
          <stop offset="0.5" stop-color="#d936b8"/>
          <stop offset="1" stop-color="#b62fd0" stop-opacity="0"/>
        </radialGradient>
      </defs>
      <circle cx="340" cy="404" r="500" fill="url(#ring-fill)" opacity="0.35"/>
      <circle cx="340" cy="404" r="420" fill="none" stroke="var(--ring-dark)" stroke-width="10" opacity="0.7"/>
      <circle cx="340" cy="404" r="340" fill="#c530c4" opacity="0.35"/>
      <circle cx="340" cy="404" r="340" fill="none" stroke="var(--ring-dark)" stroke-width="10" opacity="0.75"/>
      <circle cx="340" cy="404" r="262" fill="#a92bc8" opacity="0.35"/>
      <circle cx="340" cy="404" r="262" fill="none" stroke="var(--ring-dark)" stroke-width="9" opacity="0.75"/>
      <circle cx="340" cy="404" r="190" fill="#8d27bf" opacity="0.35"/>
    </svg>

    <div class="butterfly" style="left:60px;top:70px;width:60px;height:56px" role="img" aria-label="Small white line-drawn butterfly"></div>
    <div class="butterfly" style="left:436px;top:62px;width:112px;height:100px" role="img" aria-label="White line-drawn butterfly"></div>
    <div class="butterfly" style="left:470px;top:720px;width:112px;height:104px" role="img" aria-label="White line-drawn butterfly"></div>

    <div class="pearl" style="left:264px;top:68px;width:48px;height:48px" role="img" aria-label="Iridescent pearl"></div>
    <div class="pearl" style="left:14px;top:228px;width:52px;height:52px" role="img" aria-label="Iridescent pearl"></div>
    <div class="pearl" style="left:320px;top:760px;width:78px;height:78px" role="img" aria-label="Iridescent pearl"></div>
    <div class="pearl" style="left:604px;top:676px;width:46px;height:46px" role="img" aria-label="Iridescent pearl"></div>

    <p class="label doors">Doors open at 6:30pm</p>
    <p class="label date">October 13th, 2022 at The Bramwell</p>
    <p class="label rsvp">RSVP by September 20th</p>

    <h1 class="annual">ANNUAL</h1>

    <div class="disco-ball" role="img" aria-label="Pink mirrored disco ball"></div>

    <svg class="title" viewBox="0 0 640 300" aria-label="MRHT">
      <defs>
        <linearGradient id="silver" x1="0" y1="0" x2="0" y2="1">
          <stop offset="0" stop-color="#f4f4f4"/>
          <stop offset="0.45" stop-color="#b9b9b9"/>
          <stop offset="0.55" stop-color="#8e8e8e"/>
          <stop offset="1" stop-color="#e6e6e6"/>
        </linearGradient>
      </defs>
      <text x="58" y="258" textLength="528" lengthAdjust="spacingAndGlyphs" fill="#3b3b3b" opacity="0.6">MRHT</text>
      <text x="52" y="250" textLength="528" lengthAdjust="spacingAndGlyphs" fill="url(#silver)" stroke="#6e6e6e" stroke-width="2">MRHT</text>
    </svg>

    <div class="band-event">FUNDRAISER DINNER</div>
    <div class="band-host">The Marisol Hendrick Trust</div>

    <div class="host-mark"><span class="dot"></span>The Marisol Hendrick Trust</div>

    <p class="label price">$135 per ticket</p>
  </main>
</body>
</html>
```